Corvanel Hand Sanitizer - Label Design

hand sanitizer label -the brand is Corvanel, I'm looking to make a hand sanitizer label that will look nice and clean not too fancy with design that when you look at it you think about: clean healthy, germ free, I would like to do it with transparent background design that will look good in greenish color (with aloe) and or blueish color (refreshing scent) maybe even yellowish color(with lemon scent) only one main
color not together
Bottle size: 8oz (see attach)
Label size: 3 inches Height , 5 inches Width (see attach)
Target Market(s)
all people all ages
Industry/Entity Type
Health Product
Font styles to use
Requirements
Must have
- 1. label size is 3 inches Height , 5 inches Width Please see attach
2. to add Drog facts on the label
3. on the bottom of the frog facts change to Manufacture For:
4. one version for lemon version and one for Aloe version
Corvanel 4817 W Halberd Ave Las Vegas NV 89146
- will need to have the words: hand sanitizer
- will need to look good as blueish color and or greenish color
- play with the name Corvanel in attractive way maybe larger X or Corva-neL or something like that
- the words: kill 99.9% germs
- the words: 70% alcohol
- the words: corvanelus.example (very small letters on the bottom of the label)
- the words: vitamin E & aloe
- the words: 8oz ( 236mil )on the lower area of the label
*transparent label
Nice to have
- - a small carton of sick germ or scared germ (see example on the attach)
- of maybe on the side some clean bubbles or something that will give clean feeling
- maybe aloe leaf
Should not have
- it should not have childish look
open for ideas

```html
<!DOCTYPE html>
<html lang="en">
<head>
<meta charset="utf-8">
<title>Corvanel Hand Sanitizer Label</title>
<link rel="stylesheet" href="https://fonts.googleapis.com/css2?family=Oswald:wght@500;600&family=Montserrat:wght@700;800&family=Quicksand:wght@500;600&display=swap">
<style>
  :root {
    --stage: #eef1ee;
    --label: #ffffff;
    --green-dark: #1fa444;
    --green-light: #7cc242;
    --title-green: #4ea23e;
    --alcohol-red: #cc2229;
    --brand-blue: #1a7fc1;
    --ink: #1c1c1c;
    --silver-a: #c4c4c4;
    --silver-b: #f2f2f2;
    --shield-a: #5cc0ec;
    --shield-b: #1a75b8;
    --aloe-a: #8fce5a;
    --aloe-b: #3f9a2f;
  }
  * { box-sizing: border-box; margin: 0; padding: 0; }
  html, body {
    width: 1200px; height: 780px; overflow: hidden;
    background: var(--stage);
  }
  .canvas { position: relative; width: 1200px; height: 780px; }
  .label {
    position: absolute; left: 410px; top: 38px;
    width: 380px; height: 704px;
    background: var(--label);
    border-radius: 20px;
    overflow: hidden;
    box-shadow: 0 6px 24px rgba(0,0,0,0.08);
  }
  .top-band { position: absolute; left: 0; top: 0; width: 380px; height: 170px; }
  .aloe-art {
    position: absolute; right: 0; top: 0; width: 120px; height: 95px;
    background: linear-gradient(200deg, var(--aloe-a), var(--aloe-b) 70%, transparent);
    clip-path: polygon(100% 0, 100% 25%, 40% 95%, 20% 80%, 70% 20%);
    opacity: 0.85;
  }
  .claim {
    position: absolute; left: 38px; top: 34px;
    font-family: Montserrat, Arial, sans-serif; font-weight: 700;
    font-size: 21px; color: #fff; white-space: nowrap;
  }
  .brand {
    position: absolute; left: 0; right: 0; top: 146px;
    text-align: center;
    font-family: Montserrat, Arial, sans-serif; font-weight: 800;
    font-size: 48px; color: var(--brand-blue);
  }
  .condensed { display: inline-block; transform-origin: left top; white-space: nowrap; }
  .product-name {
    position: absolute; left: 38px; top: 262px;
    font-family: Oswald, "Arial Narrow", sans-serif; font-weight: 600;
    font-size: 74px; line-height: 76px; color: var(--title-green);
    letter-spacing: -1px;
  }
  .product-name .condensed { transform: scaleX(0.84); }
  .alcohol {
    position: absolute; left: 44px; top: 410px;
    font-family: Oswald, "Arial Narrow", sans-serif; font-weight: 500;
    font-size: 38px; line-height: 44px; color: var(--alcohol-red);
  }
  .alcohol .condensed { transform: scaleX(0.76); }
  .germ-badge {
    position: absolute; left: 237px; top: 485px; width: 93px; height: 124px;
    background: linear-gradient(160deg, var(--shield-a), var(--shield-b));
    clip-path: polygon(0 8%, 50% 0, 100% 8%, 100% 68%, 50% 100%, 0 68%);
  }
  .germ-claim {
    position: absolute; left: 224px; top: 572px;
    font-family: Oswald, "Arial Narrow", sans-serif; font-weight: 500;
    font-size: 25px; line-height: 30px; color: var(--ink);
  }
  .germ-claim .condensed { transform: scaleX(0.7); }
  .volume {
    position: absolute; left: 38px; top: 617px;
    font-family: Quicksand, Arial, sans-serif; font-weight: 600;
    font-size: 21px; color: var(--ink); white-space: nowrap;
  }
  .silver-rule {
    position: absolute; left: 0; top: 664px; width: 380px; height: 8px;
    background: linear-gradient(90deg, var(--silver-a), var(--silver-b) 50%, var(--silver-a));
  }
  .bottom-band {
    position: absolute; left: 0; top: 672px; width: 380px; height: 32px;
    background: linear-gradient(90deg, var(--green-light), var(--green-dark) 50%, var(--green-light));
    color: #fff; text-align: center;
    font-family: Quicksand, Arial, sans-serif; font-weight: 600;
    font-size: 15px; line-height: 32px;
  }
</style>
</head>
<body>
<div class="canvas">
  <div class="label">
    <svg class="top-band" viewBox="0 0 380 170" aria-hidden="true">
      <defs>
        <linearGradient id="bandGreen" x1="0" y1="0" x2="1" y2="0">
          <stop offset="0" stop-color="#66bb44"/>
          <stop offset="0.45" stop-color="#1fa444"/>
          <stop offset="1" stop-color="#7cc242"/>
        </linearGradient>
        <linearGradient id="silver" x1="0" y1="0" x2="1" y2="0">
          <stop offset="0" stop-color="#bdbdbd"/>
          <stop offset="0.5" stop-color="#f0f0f0"/>
          <stop offset="1" stop-color="#bdbdbd"/>
        </linearGradient>
      </defs>
      <path d="M0 0 H380 V150 Q190 26 0 150 Z" fill="url(#bandGreen)"/>
      <path d="M0 156 Q190 32 380 156" fill="none" stroke="url(#silver)" stroke-width="8"/>
    </svg>
    <div class="aloe-art" role="img" aria-label="Cut aloe vera leaf"></div>
    <p class="claim">WITH VITAMIN E AND ALOE</p>
    <p class="brand">Corvanel</p>
    <h1 class="product-name"><span class="condensed">HAND<br>SANITIZER</span></h1>
    <p class="alcohol"><span class="condensed">70% Alcohol</span></p>
    <div class="germ-badge" role="img" aria-label="Blue shield with a crossed-out cartoon germ"></div>
    <p class="germ-claim"><span class="condensed">Kill 99.9% Germs</span></p>
    <p class="volume">8oz ( 236mil )</p>
    <div class="silver-rule"></div>
    <div class="bottom-band">corvanelus.example</div>
  </div>
</div>
</body>
</html>
```